Business Card Design

We need a design that will also transfer to car decals
We need a design that will speak to the average person needing home and office remodeling
The design should be fresh, exciting, easy to read in a glance and unique
We would like a die-cut tool belt
Bright colors and evenly spaced information

Target Market(s)

Home and business owners
Middle and Upper Income property owners
Families and people with fixer upper homes

Industry/Entity Type

Business

Contact Information for Business Card

Looking for the best Bay Area Handyman? Here I am!
RKW Handyman Services does it all at prices regular people can afford.
Electrical, Plumbing, Carpentry, Remodeling, Fencing, Picture and window placement, Hauling ... and anything else you can imagine!
510-374-2196
Serving the Entire Bay Area
Free Estimates! Call us Today to turn your dreams into reality!

Font styles to use
Serif

Requirements
Must have
• Speaks to the average person
stands out among similar industry cards
Nice to have
• fun, comical, you want to hold on to this card
Should not have
• bland colors
look too crowded

```html
<!DOCTYPE html>
<html lang="en">
<head>
<meta charset="utf-8">
<title>RKW Handyman Services – Business Card</title>
<link href="https://fonts.googleapis.com/css2?family=Tinos:wght@400;700&display=swap" rel="stylesheet">
<style>
  :root {
    --orange: #f26522;
    --white: #ffffff;
    --ink: #111111;
    --backdrop: #e8e3db;
    --leather-dark: #5a2a17;
    --leather-light: #9a4a2a;
  }
  * { box-sizing: border-box; margin: 0; padding: 0; }
  html, body { width: 1200px; height: 846px; overflow: hidden; }
  body {
    background: var(--backdrop);
    font-family: "Tinos", serif;
    color: var(--ink);
    position: relative;
  }
  .card {
    position: absolute;
    width: 660px;
    height: 376px;
    background: var(--white);
    border-radius: 28px;
    overflow: hidden;
    box-shadow: 0 3px 10px rgba(0,0,0,0.18);
  }
  .card--front { left: 60px; top: 50px; }
  .card--back { left: 490px; top: 430px; }

  /* Front: brand column */
  .brand {
    position: absolute;
    left: 0; top: 0;
    width: 236px; height: 100%;
    display: flex; flex-direction: column; align-items: center;
  }
  .brand__name {
    margin-top: 92px;
    text-align: center;
    color: var(--orange);
    font-weight: 700;
    font-size: 30px;
    line-height: 1.05;
  }
  .brand__name-lead { display: block; font-size: 64px; letter-spacing: 2px; }
  .brand__call {
    margin-top: 52px;
    text-align: center;
    font-size: 17px;
    line-height: 1.15;
  }
  .brand__phone {
    margin-top: 8px;
    font-size: 23px;
  }

  /* Front: message column */
  .headline {
    position: absolute;
    left: 236px; right: 0; top: 18px;
    text-align: center;
  }
  .headline__kicker { font-weight: 700; font-size: 14px; letter-spacing: 0.2px; }
  .headline__main { font-size: 30px; margin-top: 4px; }
  .services {
    position: absolute;
    left: 236px; right: 0; top: 96px; bottom: 0;
    background: var(--orange);
    color: var(--white);
    padding: 10px 22px 0 60px;
    border-top-left-radius: 6px;
  }
  .services__intro { font-size: 19px; line-height: 1.2; text-align: center; }
  .services__list {
    list-style: none;
    margin-top: 8px;
    font-size: 17px;
    line-height: 1.12;
  }
  .services__list li { position: relative; padding-left: 32px; }
  .services__list li::before {
    content: "";
    position: absolute; left: -22px; top: 8px;
    width: 5px; height: 5px; border-radius: 50%;
    background: var(--white);
  }
  .services__list .services__more { padding-left: 36px; }

  /* Back */
  .belt-photo {
    position: absolute;
    left: 130px; top: 50px;
    width: 390px; height: 220px;
    border-radius: 18px;
    background: radial-gradient(ellipse at 50% 45%, var(--leather-light), var(--leather-dark) 75%, rgba(90,42,23,0) 100%);
  }
  .back-brand {
    position: absolute;
    right: 24px; bottom: 70px;
    text-align: center;
    color: var(--orange);
    font-weight: 700;
    font-size: 12px;
    line-height: 1.05;
  }
  .back-brand__lead { display: block; font-size: 34px; letter-spacing: 1px; }
  .back-tagline {
    position: absolute;
    left: 0; right: 70px; bottom: 26px;
    text-align: center;
    font-weight: 700;
    font-size: 16px;
    letter-spacing: 0.4px;
  }
</style>
</head>
<body>
  <section class="card card--front">
    <div class="brand">
      <p class="brand__name"><span class="brand__name-lead">RKW</span>Handyman Services</p>
      <p class="brand__call">Call us Today to turn your<br>dreams into reality!</p>
      <p class="brand__phone">510-374-2196</p>
    </div>
    <header class="headline">
      <p class="headline__kicker">LOOKING FOR THE BEST BAY AREA HANDYMAN?</p>
      <p class="headline__main">Here I am!</p>
    </header>
    <div class="services">
      <p class="services__intro">RKW Handyman Services does it all<br>at prices regular people can afford.</p>
      <ul class="services__list">
        <li>Electrical</li>
        <li>Plumbing</li>
        <li>Carpentry</li>
        <li>Remodeling</li>
        <li>Fencing</li>
        <li>Picture and window placement</li>
        <li>Hauling</li>
        <li class="services__more">and anything else you can imagine!<br>Serving the Entire Bay Area Free Estimates!</li>
      </ul>
    </div>
  </section>

  <section class="card card--back">
    <div class="belt-photo" role="img" aria-label="Photo of a brown leather tool belt loaded with hand tools"></div>
    <p class="back-brand"><span class="back-brand__lead">RKW</span>Handyman Services</p>
    <p class="back-tagline">SERVING THE ENTIRE BAY AREA FREE ESTIMATES!</p>
  </section>
</body>
</html>
```